New Look and Feel for 82 year old Varrenko Ltd. presentations

We are seeking new ideas to have powerpoint-layouts for the group headquarters. Varrenko is an industrial company in maritime, hydraulics, heavy machinery and industrial services. Please read our history and watch the video for a quick familiarization. http://www.varrenko-example.fi/eng/main.php

Our customer relationships are based on trust, with Varrenko providing to customers, cooperation partners and other interest groups products and solutions that produce sustainable benefits.

Varrenko strives to ensure that the environmental impact of the products is considered over the entire life cycle and the processes used by the Group are as environmentally benign as possible.

Industry/Entity Type

It Company

Colors

Designer to choose colors to be used in the design.

Requirements
Must have
• Logo
Nice to have
• example animations and transitions

```html
<!DOCTYPE html>
<html lang="en">
<head>
<meta charset="utf-8">
<title>Varrenko Ltd. – presentation layouts</title>
<link rel="stylesheet" href="https://fonts.googleapis.com/css2?family=Oswald:wght@400;500;600&family=Open+Sans:wght@400;600&display=swap">
<style>
  :root{
    --red:#d11b22;
    --red-bright:#e8403f;
    --red-deep:#a50f16;
    --charcoal:#37373b;
    --ink:#1e1e20;
    --paper:#ececec;
    --paper-light:#f6f6f6;
    --grey:#5a5a5e;
    --white:#ffffff;
    --label:#333333;
  }
  *{margin:0;padding:0;box-sizing:border-box}
  html,body{width:1200px;height:1003px;overflow:hidden;background:var(--white)}
  .board{position:relative;width:1200px;height:1003px}
  .slide{position:absolute;width:563px;height:423px;box-shadow:0 2px 6px rgba(0,0,0,.25);overflow:hidden}
  .slide svg{display:block;width:563px;height:423px}
  .slide--cover{left:21px;top:22px}
  .slide--back{left:613px;top:22px}
  .slide--p1{left:21px;top:506px}
  .slide--p2{left:613px;top:506px}
  .slide-label{position:absolute;width:563px;text-align:center;font-family:'Open Sans',Arial,sans-serif;font-size:25px;color:var(--label)}
  .label--cover{left:21px;top:458px}
  .label--back{left:613px;top:458px}
  .label--p1{left:21px;top:936px}
  .label--p2{left:613px;top:936px}
  .head{font-family:'Oswald',sans-serif}
  .body{font-family:'Open Sans',Arial,sans-serif}
  .para{font-family:'Open Sans',Arial,sans-serif;font-size:8.6px;line-height:12.3px;color:#333;text-align:justify}
  .para p+p{margin-top:12px}
  .note{font-family:'Open Sans',Arial,sans-serif;font-size:8.4px;line-height:12.2px;color:#333;text-align:justify}
</style>
</head>
<body>
<div class="board">

  <!-- Cover -->
  <div class="slide slide--cover">
    <svg viewBox="0 0 704 529" xmlns="http://www.w3.org/2000/svg">
      <defs>
        <linearGradient id="paperGrad" x1="0" y1="0" x2="0" y2="1">
          <stop offset="0" stop-color="#f4f4f4"/><stop offset="1" stop-color="#e4e4e4"/>
        </linearGradient>
        <linearGradient id="sparkGrad" x1="0" y1="0" x2="1" y2="1">
          <stop offset="0" stop-color="#1a1410"/><stop offset=".45" stop-color="#6a3a12"/><stop offset=".7" stop-color="#3c3c44"/><stop offset="1" stop-color="#8c8f96"/>
        </linearGradient>
      </defs>
      <rect width="704" height="529" fill="url(#paperGrad)"/>
      <rect x="0" y="117" width="704" height="49" fill="var(--red)"/>
      <rect x="0" y="0" width="140" height="166" fill="var(--red)"/>
      <rect x="0" y="166" width="704" height="179" fill="var(--charcoal)"/>
      <g role="img" aria-label="Photo of a technician grinding a large steel gear ring with sparks flying">
        <polygon points="230,166 704,166 704,397 360,397" fill="url(#sparkGrad)"/>
      </g>
      <polygon points="372,397 704,397 704,529 446,529" fill="var(--charcoal)"/>
      <polygon points="133,0 205,0 420,467 350,467" fill="var(--red-bright)"/>
      <polygon points="205,0 225,0 440,467 420,467" fill="var(--red-deep)" opacity=".85"/>
      <text class="head" x="480" y="80" font-size="48" font-weight="600" fill="var(--ink)" text-anchor="middle">Varrenko</text>
      <text class="head" x="27" y="246" font-size="19" font-weight="400" fill="var(--white)">ENGINEERING WORKS</text>
      <text class="body" x="27" y="263" font-size="8.6" fill="var(--white)">Varrenko Works is a business group which</text>
      <text class="body" x="27" y="275" font-size="8.6" fill="var(--white)">provides turnkey services of the mechanical</text>
      <text class="body" x="27" y="287" font-size="8.6" fill="var(--white)">engineering industry.</text>
      <text class="head" x="26" y="414" font-size="32" font-weight="500" fill="var(--ink)">LOREM IPSUM IS</text>
      <text class="head" x="26" y="449" font-size="32" font-weight="500" fill="var(--ink)">SIMPLY <tspan fill="var(--red)">DUMMY TEXT</tspan></text>
      <rect x="18" y="461" width="283" height="25" fill="var(--ink)"/>
      <text class="head" x="28" y="480" font-size="16" fill="var(--white)">2018 LOREM IPSUM IS SIMPLY DUMMY</text>
      <line x1="410" y1="492" x2="522" y2="492" stroke="var(--white)" stroke-width="1"/>
      <circle cx="536" cy="491" r="7" fill="none" stroke="var(--white)" stroke-width="1.5"/>
      <text class="body" x="688" y="495" font-size="10" font-weight="600" fill="var(--white)" text-anchor="end">www.varrenko-example.fi</text>
    </svg>
  </div>
  <div class="slide-label label--cover">cover</div>

  <!-- Back -->
  <div class="slide slide--back">
    <svg viewBox="0 0 704 529" xmlns="http://www.w3.org/2000/svg">
      <rect width="704" height="529" fill="url(#paperGrad)"/>
      <rect width="704" height="166" fill="var(--red)"/>
      <rect y="166" width="704" height="179" fill="var(--charcoal)"/>
      <text class="head" x="352" y="112" font-size="56" font-weight="600" fill="var(--white)" text-anchor="middle">Varrenko</text>
      <text class="head" x="352" y="226" font-size="26" fill="var(--white)" text-anchor="middle">LOREM IPSUM IS</text>
      <text class="head" x="352" y="256" font-size="26" fill="var(--red-bright)" text-anchor="middle">LOREM IPSUM IS SIMPLY</text>
      <line x1="312" y1="268" x2="392" y2="268" stroke="var(--white)" stroke-width="1.5"/>
      <text class="body" x="352" y="292" font-size="8.6" fill="var(--white)" text-anchor="middle">Lorem Ipsum is simply dummy text of the printing and typesetting industry. Lorem</text>
      <text class="body" x="352" y="304" font-size="8.6" fill="var(--white)" text-anchor="middle">Ipsum has been the industry's standard dummy text ever since the 1500s</text>
      <text class="head" x="352" y="394" font-size="28" fill="var(--red)" text-anchor="middle">CALL US TODAY <tspan fill="var(--ink)">020 555 0147</tspan></text>
      <circle cx="263" cy="417" r="4" fill="var(--ink)"/>
      <text class="body" x="272" y="421" font-size="11" fill="var(--ink)">Varrenko Oy, Satamakatu 27, PL 8</text>
      <text class="body" x="359" y="444" font-size="11" fill="var(--ink)" text-anchor="middle">FI-26999 KIVIRANTA</text>
      <line x1="150" y1="493" x2="276" y2="493" stroke="var(--ink)" stroke-width="1"/>
      <text class="body" x="359" y="497" font-size="10" font-weight="600" fill="var(--ink)" text-anchor="middle">www.varrenko-example.fi</text>
      <line x1="442" y1="493" x2="560" y2="493" stroke="var(--ink)" stroke-width="1"/>
    </svg>
  </div>
  <div class="slide-label label--back">back</div>

  <!-- Page 01 -->
  <div class="slide slide--p1">
    <svg viewBox="0 0 704 529" xmlns="http://www.w3.org/2000/svg">
      <defs>
        <linearGradient id="officeGrad" x1="0" y1="0" x2="1" y2="1">
          <stop offset="0" stop-color="#b79a84"/><stop offset=".4" stop-color="#8a8886"/><stop offset="1" stop-color="#4a4a4e"/>
        </linearGradient>
        <linearGradient id="skyGrad" x1="0" y1="0" x2="0" y2="1">
          <stop offset="0" stop-color="#3f6fb5"/><stop offset="1" stop-color="#8fb0d8"/>
        </linearGradient>
      </defs>
      <g role="img" aria-label="Photo of a man in glasses working at a desk in an office">
        <rect width="704" height="529" fill="url(#officeGrad)"/>
      </g>
      <polygon points="704,25 704,529 0,529 0,500" fill="var(--charcoal)"/>
      <polygon points="164,46 278,112 278,244 164,310 50,244 50,112" fill="var(--white)" opacity=".35"/>
      <polygon points="164,58 268,118 268,238 164,298 60,238 60,118" fill="var(--red)" opacity=".92"/>
      <text class="head" x="76" y="167" font-size="28" fill="var(--white)">LOREM IPSUM</text>
      <text class="head" x="76" y="203" font-size="34" fill="var(--white)">LOREM IPSUM</text>
      <polyline points="110,222 164,252 218,222" fill="none" stroke="var(--white)" stroke-width="1" opacity=".8"/>
      <g role="img" aria-label="Photo of a seagull flying against a blue sky">
        <rect x="312" y="130" width="148" height="308" fill="url(#skyGrad)"/>
      </g>
      <rect x="322" y="270" width="132" height="160" fill="var(--paper-light)"/>
      <foreignObject x="328" y="276" width="122" height="152">
        <div xmlns="http://www.w3.org/1999/xhtml">
          <div class="head" style="font-size:15px;color:var(--ink);margin-bottom:6px">LOREM IPSUM</div>
          <div class="note">Lorem Ipsum is simply dummy text of the printing and typesetting industry. Lorem Ipsum has been the industry's. Lorem Ipsum is simply dummy text of the printing and typesetting industry. Lorem Ipsum has been the industry's.</div>
        </div>
      </foreignObject>
      <g class="feature">
        <polygon points="540,206 677,206 677,250 560,250" fill="var(--red)"/>
        <polygon points="514,200 540,214 540,242 514,256 488,242 488,214" fill="var(--red-deep)"/>
        <circle cx="514" cy="228" r="10" fill="var(--white)"/>
        <polygon points="547,244 557,250 557,262 547,268 537,262 537,250" fill="none" stroke="var(--red-deep)" stroke-width="2"/>
        <text class="head" x="592" y="224" font-size="8" fill="var(--white)">LOREM IPSUM SIMPLY</text>
        <text class="body" x="592" y="235" font-size="6" fill="var(--white)">Lorem ipsum simply</text>
        <text class="body" x="592" y="243" font-size="6" fill="var(--white)">dummy text.</text>
      </g>
      <g class="feature">
        <polygon points="540,292 677,292 677,336 560,336" fill="var(--red)"/>
        <polygon points="514,286 540,300 540,328 514,342 488,328 488,300" fill="var(--red-deep)"/>
        <rect x="502" y="307" width="24" height="14" rx="4" fill="var(--white)"/>
        <polygon points="547,330 557,336 557,348 547,354 537,348 537,336" fill="none" stroke="var(--red-deep)" stroke-width="2"/>
        <text class="head" x="592" y="310" font-size="8" fill="var(--white)">LOREM IPSUM SIMPLY</text>
        <text class="body" x="592" y="321" font-size="6" fill="var(--white)">Lorem ipsum simply</text>
        <text class="body" x="592" y="329" font-size="6" fill="var(--white)">dummy text.</text>
      </g>
      <g class="feature">
        <polygon points="540,378 677,378 677,422 560,422" fill="var(--red)"/>
        <polygon points="514,372 540,386 540,414 514,428 488,414 488,386" fill="var(--red-deep)"/>
        <circle cx="506" cy="400" r="5" fill="var(--white)"/><circle cx="514" cy="396" r="6" fill="var(--white)"/><circle cx="522" cy="400" r="5" fill="var(--white)"/>
        <rect x="502" y="404" width="24" height="7" rx="3" fill="var(--white)"/>
        <polygon points="547,416 557,422 557,434 547,440 537,434 537,422" fill="none" stroke="var(--red-deep)" stroke-width="2"/>
        <text class="head" x="592" y="396" font-size="8" fill="var(--white)">LOREM IPSUM SIMPLY</text>
        <text class="body" x="592" y="407" font-size="6" fill="var(--white)">Lorem ipsum simply</text>
        <text class="body" x="592" y="415" font-size="6" fill="var(--white)">dummy text.</text>
      </g>
      <line x1="150" y1="493" x2="276" y2="493" stroke="var(--white)" stroke-width="1"/>
      <text class="body" x="357" y="497" font-size="10" font-weight="600" fill="var(--white)" text-anchor="middle">www.varrenko-example.fi</text>
      <line x1="440" y1="493" x2="560" y2="493" stroke="var(--white)" stroke-width="1"/>
      <text class="body" x="670" y="497" font-size="10" fill="var(--white)" text-anchor="middle">01</text>
    </svg>
  </div>
  <div class="slide-label label--p1">page 01</div>

  <!-- Page 02 -->
  <div class="slide slide--p2">
    <svg viewBox="0 0 704 529" xmlns="http://www.w3.org/2000/svg">
      <rect width="704" height="529" fill="var(--charcoal)"/>
      <rect x="27" y="44" width="650" height="429" fill="url(#paperGrad)"/>
      <line x1="48" y1="72" x2="48" y2="118" stroke="var(--ink)" stroke-width="1.5"/>
      <text class="head" x="56" y="97" font-size="29" fill="var(--ink)">LOREM IPSUM</text>
      <text class="head" x="56" y="116" font-size="15" fill="var(--red)">LOREM IPSUM IS SIMPLY</text>
      <foreignObject x="46" y="141" width="228" height="300">
        <div xmlns="http://www.w3.org/1999/xhtml" class="para">
          <p>Lorem Ipsum is simply dummy text of the printing and typesetting industry. Lorem Ipsum has been the industry's standard dummy text ever since the 1500s, when an unknown printer took a galley of type and scrambled it to make a type specimen book. It has survived not only five centuries, but also the leap into electronic typesetting, remaining essentially unchanged. It was popularised in the 1960s with the release of Letraset sheets containing Lorem Ipsum passages, and more recently with desktop publishing.</p>
          <p>Lorem Ipsum is simply dummy text of the printing and typesetting industry. Lorem Ipsum has been the industry's standard dummy text ever since the 1500s, when an unknown printer took a galley of type and scrambled it to make a type specimen book. It has survived not only five centuries, but also the leap into electronic typesetting, remaining essentially unchanged. It was popularised in the 1960s with the release of Letraset sheets containing Lorem Ipsum passages, and more recently with desktop publishing.</p>
        </div>
      </foreignObject>
      <line x1="403" y1="72" x2="403" y2="118" stroke="var(--ink)" stroke-width="1.5"/>
      <text class="head" x="411" y="97" font-size="29" fill="var(--ink)">LOREM IPSUM</text>
      <text class="head" x="411" y="116" font-size="15" fill="var(--red)">LOREM IPSUM IS SIMPLY</text>
      <text class="body" x="486" y="148" font-size="12" fill="var(--ink)" text-anchor="middle">Lorem Ipsum is simply dummy text</text>
      <g class="ring" stroke="var(--paper)" stroke-width="3">
        <path d="M420,439.2 A140 140 0 0 1 352.1,342.3 L419.1,330.5 A72 72 0 0 0 454,380.4 Z" fill="#c4141c"/>
        <path d="M352.1,342.3 A140 140 0 0 1 382.8,228 L434.8,271.7 A72 72 0 0 0 419.1,330.5 Z" fill="var(--red)"/>
        <path d="M382.8,228 A140 140 0 0 1 490,178 L490,246 A72 72 0 0 0 434.8,271.7 Z" fill="var(--red-deep)"/>
        <path d="M490,178 A140 140 0 0 1 597.2,228 L545.2,271.7 A72 72 0 0 0 490,246 Z" fill="#9e0d14"/>
        <path d="M597.2,228 A140 140 0 0 1 627.9,342.3 L560.9,330.5 A72 72 0 0 0 545.2,271.7 Z" fill="var(--grey)"/>
        <path d="M627.9,342.3 A140 140 0 0 1 560,439.2 L526,380.4 A72 72 0 0 0 560.9,330.5 Z" fill="#2a2a2c"/>
      </g>
      <g class="ring-labels body" font-size="7" fill="var(--white)" text-anchor="middle">
        <circle cx="403" cy="364" r="6" fill="var(--white)"/>
        <text x="403" y="382">lorem ipsum</text><text x="403" y="390">simply</text><text x="403" y="398">dummy</text>
        <circle cx="388" cy="276" r="6" fill="var(--white)"/>
        <text x="388" y="294">lorem ipsum</text><text x="388" y="302">simply</text><text x="388" y="310">dummy</text>
        <rect x="439" y="203" width="12" height="10" fill="var(--white)"/>
        <text x="445" y="226">lorem ipsum simply</text>
        <rect x="529" y="203" width="12" height="10" fill="var(--white)"/>
        <text x="535" y="222">lorem ipsum</text><text x="535" y="229">simply</text><text x="535" y="236">dummy</text>
        <circle cx="592" cy="276" r="6" fill="var(--white)"/>
        <text x="592" y="294">lorem ipsum</text><text x="592" y="302">simply</text><text x="592" y="310">dummy</text>
        <circle cx="577" cy="364" r="6" fill="var(--white)"/>
        <text x="577" y="382">lorem ipsum</text><text x="577" y="390">simply</text><text x="577" y="398">dummy</text>
      </g>
      <circle cx="490" cy="264" r="8" fill="#f5c518"/>
      <rect x="486" y="272" width="8" height="5" fill="var(--ink)"/>
      <text class="head" x="490" y="318" font-size="38" fill="var(--grey)" text-anchor="middle">LOREM</text>
      <text class="head" x="490" y="360" font-size="38" fill="var(--grey)" text-anchor="middle">IPSUM</text>
      <text class="body" x="490" y="424" font-size="10.5" fill="var(--ink)" text-anchor="middle">Lorem Ipsum is simply</text>
      <line x1="150" y1="493" x2="276" y2="493" stroke="var(--white)" stroke-width="1"/>
      <text class="body" x="358" y="497" font-size="10" font-weight="600" fill="var(--white)" text-anchor="middle">www.varrenko-example.fi</text>
      <line x1="441" y1="493" x2="560" y2="493" stroke="var(--white)" stroke-width="1"/>
      <text class="body" x="670" y="497" font-size="10" fill="var(--white)" text-anchor="middle">02</text>
    </svg>
  </div>
  <div class="slide-label label--p2">page 02</div>

</div>
</body>
</html>
```